International Petrochemical business needs a web design for Clearway Desk system

We need a web design for a "Clearway Desk" system for an international petrochemical company. The web site is used internally within the company. It is hosted by an internal department which provides government permit request service for other departments.

We would like to see designs of two pages using color light blue. (home page, internal page as attached).
Home Page:
1. Header has a background image and small animation. Header on home page can be taller than the header of the internal page.
2. Layout as attached.

Internal Page:
1. Header can use the same background image as the home page and can be shorter to utilize the page for content.
2. The blue icon behind every captions represent an icon. When user move mouse over this icon, it displays the caption in Thai language as a tooltip. This icon needs to be redesign.

The final design should communicate the followings:
- Excellent service provided system in terms of time and accurary
- Rapid growth of business via building petrochemical refinery plant

For Internal Page, the blue circle behind every captions represent an icon. When mouse over this icon, a tool tip showing the caption in Thai language is shown. Please also design this icon..

There are more feedbacks from customer as followed:

1. Banner should consists of 
    1.1 "Approved" stamp on paper
    1.2 An image of Garuda. It is used on every government documents in Thailand
    1.3 Image of petrochemical plant
2. Each menu item (Home, Permit, Search, etc) should have different colors. Drop down menu will use the same color as its parent menu item.
3. Overall tone of the web page should be light blue with background of the body the web page in white
4. "New Request" button should use green color with icon on it
5. Table header of each box in the body of the page should use dark blue background with text in white

Please kindly submit your revisions.
Thank you.

Reason: We get some late feedbacks from customers which was just updated to all designers.

• 1. Design for 1024x768 screen resolution
2. Use light blue theme
3. Background of header where the company logo is must have white background

```html
<!DOCTYPE html>
<html lang="en">
<head>
<meta charset="utf-8">
<title>Clearway Desk – Request Form</title>
<link rel="stylesheet" href="https://fonts.googleapis.com/css2?family=Open+Sans:wght@400;600;700&family=Sarabun:wght@400&display=swap">
<style>
:root{
  --brand:#1a9ee0;
  --brand-dark:#0d5aa7;
  --navy:#0e3570;
  --panel:#eef7fd;
  --ink:#222;
  --muted:#555;
  --field-border:#b9b9b9;
  --chip:#c9c9c9;
  --rule:#cfd6dc;
  --req:#e0262b;
  --tab-home:#3cb7e0;
  --tab-permits:#22c08a;
  --tab-search:#f3a51b;
  --tab-report:#e33a3a;
  --tab-admin:#4dbb3a;
  --tab-help:#9b3bc4;
  --white:#fff;
}
*{box-sizing:border-box;margin:0;padding:0}
html,body{width:918px;height:1200px;overflow:hidden;background:var(--white)}
body{font-family:"Open Sans",Arial,sans-serif;color:var(--ink);font-size:13px}
.canvas{position:relative;width:918px;height:1200px;overflow:hidden}
.abs{position:absolute}

/* header */
.top-rule{left:0;top:0;width:918px;height:4px;background:var(--brand-dark)}
.brand{left:48px;top:22px;display:flex;align-items:center;gap:8px}
.brand-dot{width:26px;height:26px;border-radius:50%;background:var(--brand)}
.brand-name{font-weight:700;font-size:17px;color:var(--brand);letter-spacing:.2px}
.system-title{right:38px;top:30px;font-weight:700;font-size:30px;color:var(--brand);letter-spacing:.5px}
.nav{left:36px;top:75px;height:27px}
.nav a{position:absolute;top:0;width:81px;height:27px;border-radius:6px 6px 0 0;color:var(--white);font-weight:700;font-size:12.5px;text-align:center;line-height:28px;text-decoration:none;text-shadow:0 1px 1px rgba(0,0,0,.25);box-shadow:inset 0 10px 8px rgba(255,255,255,.28)}
.nav-rule{left:0;top:102px;width:918px;height:1px;background:var(--rule)}

/* panel */
.panel{left:36px;top:140px;width:850px;height:994px;background:var(--panel);border:1px solid #d6e6f0;border-radius:4px;box-shadow:0 1px 3px rgba(0,0,0,.12)}
.panel-head{left:36px;top:140px;width:850px;height:40px;border-radius:4px 4px 0 0;background:linear-gradient(#27b2ec,#0d93d6);color:var(--white);font-weight:700;font-size:15px;padding:11px 0 0 13px}

.label{width:150px;text-align:right;font-weight:600;font-size:12.5px;color:var(--ink)}
.label.req::after{content:"*";color:var(--req);font-size:10px;vertical-align:top;margin-left:2px}
.colon{font-weight:700;font-size:13px}
.ico{width:30px;height:30px;border-radius:6px;background:var(--brand)}
.ico svg{display:block}

.field{height:23px;background:linear-gradient(#e9e9e9,#fff 45%);border:1px solid var(--field-border);border-radius:4px;color:var(--muted);font-size:12.5px;padding:3px 0 0 12px;white-space:nowrap}
.select::after{content:"";position:absolute;right:6px;top:7px;border-left:6px solid transparent;border-right:6px solid transparent;border-top:9px solid #777}
.area{height:82px;padding-top:6px}

.btn{height:23px;border:1px solid #aaa;border-radius:4px;background:linear-gradient(#f4f4f4,#cfcfcf);color:#555;font-size:11.5px;font-weight:600;text-align:center;line-height:21px}
.chip{height:15px;border:1px solid #b5b5b5;border-radius:2px;background:var(--chip);font-size:8.5px;font-weight:600;color:#555;line-height:13px;padding-left:4px}
.chip b{position:absolute;right:0;top:-1px;width:21px;height:15px;border:1px solid #aaa;background:#e8e8e8;text-align:center;font-size:9px;color:#333;line-height:13px}

.tooltip{left:549px;top:267px;width:148px;height:42px;background:var(--navy);border-radius:3px;color:var(--white);font-family:"Sarabun","Open Sans",sans-serif;font-size:10px;line-height:14px;padding:6px 0 0 10px}
.tooltip::before{content:"";position:absolute;left:108px;top:-6px;border-left:6px solid transparent;border-right:6px solid transparent;border-bottom:6px solid var(--navy)}

.related{left:252px;top:905px;width:361px;height:138px;background:var(--white);border:1px solid #c9d3da;border-radius:4px;overflow:hidden}
.related table{width:100%;border-collapse:collapse;font-size:12.5px}
.related th{background:var(--brand);color:var(--white);font-weight:600;text-align:left;height:27px}
.related td{height:21.7px}
.related tr:nth-child(even) td{background:#ededed}
.related th:first-child,.related td:first-child{padding-left:12px}
.related a{color:var(--brand-dark)}
.pager{height:22px;border:1px solid #d0d0d0;background:#f5f5f5;font-size:12px;color:var(--brand-dark);text-align:center;line-height:20px}
.pager.off{color:#aaa}

.action{height:31px;border:1px solid #aaa;border-radius:4px;background:linear-gradient(#f2f2f2,#cbcbcb);color:#666;font-size:14px;font-weight:600;text-align:center;line-height:29px}

.footer{left:0;top:1152px;width:918px;height:48px;background:var(--brand-dark);color:var(--white);font-size:8.5px}
.footer span{position:absolute;top:17px}
</style>
</head>
<body>
<div class="canvas">

  <div class="abs top-rule"></div>
  <div class="abs brand"><span class="brand-dot"></span><span class="brand-name">NORVALE CHEMICAL</span></div>
  <div class="abs system-title">CLEARWAY DESK</div>

  <nav class="abs nav">
    <a style="left:0;background:var(--tab-home)">HOME</a>
    <a style="left:91px;background:var(--tab-permits)">PERMITS</a>
    <a style="left:182px;background:var(--tab-search)">SEARCH</a>
    <a style="left:273px;background:var(--tab-report)">REPORT</a>
    <a style="left:364px;background:var(--tab-admin)">ADMIN</a>
    <a style="left:456px;background:var(--tab-help)">HELP</a>
  </nav>
  <div class="abs nav-rule"></div>

  <div class="abs panel"></div>
  <div class="abs panel-head">Request Form</div>

  <!-- Request Date -->
  <div class="abs label" style="left:24px;top:199px">Request Date</div>
  <div class="abs ico" style="left:203px;top:192px"><svg width="30" height="30" viewBox="0 0 30 30" fill="none" stroke="#fff" stroke-width="2"><rect x="7" y="9" width="16" height="14" rx="1"/><path d="M7 13h16M11 6v5M19 6v5"/></svg></div>
  <div class="abs colon" style="left:239px;top:198px">:</div>
  <div class="abs field" style="left:253px;top:196px;width:42px">21</div>
  <div class="abs field select" style="left:301px;top:196px;width:84px">January</div>
  <div class="abs field" style="left:391px;top:196px;width:52px">2013</div>

  <div class="abs label" style="left:411px;top:199px;width:220px">Requester Employee No</div>
  <div class="abs ico" style="left:652px;top:192px"><svg width="30" height="30" viewBox="0 0 30 30"><circle cx="15" cy="15" r="10" fill="none" stroke="#fff" stroke-width="2"/><text x="15" y="19" fill="#fff" font-size="10" font-weight="700" text-anchor="middle" font-family="Open Sans,sans-serif">10</text></svg></div>
  <div class="abs field" style="left:703px;top:196px;width:166px">1249 43935 9444</div>

  <!-- Requester Name -->
  <div class="abs label" style="left:24px;top:239px">Requester Name</div>
  <div class="abs ico" style="left:203px;top:232px"><svg width="30" height="30" viewBox="0 0 30 30" fill="none" stroke="#fff" stroke-width="2"><rect x="6" y="9" width="18" height="13" rx="1"/><circle cx="11" cy="14" r="2"/><path d="M16 13h5M16 17h5M8 20c1-2 5-2 6 0"/></svg></div>
  <div class="abs colon" style="left:239px;top:238px">:</div>
  <div class="abs field" style="left:253px;top:236px;width:233px">Alan Pryce</div>

  <div class="abs label" style="left:411px;top:239px;width:220px">Telephone</div>
  <div class="abs ico" style="left:652px;top:232px"><svg width="30" height="30" viewBox="0 0 30 30"><path d="M10 8l3 0 1 4-2 2c1 2 3 4 5 5l2-2 4 1v3c0 1-1 2-2 2-7-1-12-6-13-13 0-1 1-2 2-2z" fill="#fff"/></svg></div>
  <div class="abs field" style="left:703px;top:236px;width:166px">2417 3080 615</div>
  <div class="abs tooltip">ระหว่างดำเนินการรอดำเนินก<br>ารรอดำเนินการ</div>

  <!-- Contact No -->
  <div class="abs label" style="left:24px;top:279px">Contact No</div>
  <div class="abs ico" style="left:203px;top:272px"><svg width="30" height="30" viewBox="0 0 30 30" fill="none" stroke="#fff" stroke-width="2"><rect x="10" y="6" width="10" height="18" rx="2" transform="rotate(15 15 15)"/><circle cx="16" cy="20" r="1" fill="#fff"/></svg></div>
  <div class="abs colon" style="left:239px;top:278px">:</div>
  <div class="abs field" style="left:253px;top:276px;width:233px">0890 2217 5508</div>

  <!-- Company -->
  <div class="abs label req" style="left:24px;top:319px">Company</div>
  <div class="abs ico" style="left:203px;top:312px"><svg width="30" height="30" viewBox="0 0 30 30" fill="#fff"><rect x="6" y="8" width="5" height="14"/><rect x="13" y="8" width="5" height="14"/><rect x="20" y="8" width="4" height="14"/></svg></div>
  <div class="abs colon" style="left:239px;top:318px">:</div>
  <div class="abs field select" style="left:253px;top:316px;width:233px">Please select</div>

  <!-- Branch -->
  <div class="abs label req" style="left:24px;top:358px">Branch</div>
  <div class="abs ico" style="left:203px;top:351px"><svg width="30" height="30" viewBox="0 0 30 30" fill="none" stroke="#fff" stroke-width="2"><rect x="12" y="6" width="6" height="5"/><rect x="5" y="19" width="6" height="5"/><rect x="12" y="19" width="6" height="5"/><rect x="19" y="19" width="6" height="5"/><path d="M15 11v8M8 19v-4h14v4"/></svg></div>
  <div class="abs colon" style="left:239px;top:357px">:</div>
  <div class="abs field select" style="left:253px;top:355px;width:233px">Please select</div>

  <!-- Document Category -->
  <div class="abs label req" style="left:24px;top:398px">Document Category</div>
  <div class="abs ico" style="left:203px;top:391px"><svg width="30" height="30" viewBox="0 0 30 30" fill="none" stroke="#fff" stroke-width="2"><path d="M9 6h10l3 3v15H9z"/><path d="M12 15l2 2 4-5M12 21h6"/></svg></div>
  <div class="abs colon" style="left:239px;top:397px">:</div>
  <div class="abs field select" style="left:253px;top:395px;width:233px">Please select</div>

  <!-- Document Type -->
  <div class="abs label req" style="left:24px;top:438px">Document Type</div>
  <div class="abs ico" style="left:203px;top:431px"><svg width="30" height="30" viewBox="0 0 30 30"><path d="M9 6h9l4 4v14H9z" fill="none" stroke="#fff" stroke-width="2"/><text x="15" y="21" fill="#fff" font-size="6" font-weight="700" text-anchor="middle" font-family="Open Sans,sans-serif">doc</text></svg></div>
  <div class="abs colon" style="left:239px;top:437px">:</div>
  <div class="abs field select" style="left:253px;top:435px;width:233px">Please select</div>

  <!-- Expected Use Date -->
  <div class="abs label req" style="left:24px;top:478px">Expected Use Date</div>
  <div class="abs ico" style="left:203px;top:471px"><svg width="30" height="30" viewBox="0 0 30 30"><rect x="7" y="8" width="16" height="16" rx="1" fill="none" stroke="#fff" stroke-width="2"/><path d="M7 12h16" stroke="#fff" stroke-width="2"/><text x="15" y="22" fill="#fff" font-size="8" font-weight="700" text-anchor="middle" font-family="Open Sans,sans-serif">1</text></svg></div>
  <div class="abs colon" style="left:239px;top:477px">:</div>
  <div class="abs field" style="left:253px;top:475px;width:42px">28</div>
  <div class="abs field select" style="left:301px;top:475px;width:84px">January</div>
  <div class="abs field" style="left:391px;top:475px;width:52px">2013</div>

  <!-- Detail -->
  <div class="abs label req" style="left:24px;top:517px">Detail</div>
  <div class="abs ico" style="left:203px;top:510px"><svg width="30" height="30" viewBox="0 0 30 30" fill="none" stroke="#fff" stroke-width="2"><path d="M7 7h14v16H7zM10 11h8M10 15h5"/><path d="M15 21l8-8"/></svg></div>
  <div class="abs colon" style="left:239px;top:516px">:</div>
  <div class="abs field area" style="left:253px;top:511px;width:233px">Lorem ipsum dolor sit amet</div>

  <!-- Attachment -->
  <div class="abs label" style="left:24px;top:616px">Attachment</div>
  <div class="abs ico" style="left:203px;top:609px"><svg width="30" height="30" viewBox="0 0 30 30" fill="none" stroke="#fff" stroke-width="2"><path d="M19 10l-8 8a2 2 0 0 0 3 3l9-9a4 4 0 0 0-6-6l-9 9a6 6 0 0 0 8 8l6-6"/></svg></div>
  <div class="abs colon" style="left:239px;top:615px">:</div>
  <div class="abs field" style="left:253px;top:613px;width:233px">confidential.doc</div>
  <div class="abs btn" style="left:495px;top:613px;width:66px">BROWSE</div>
  <div class="abs btn" style="left:571px;top:613px;width:65px">ATTACH</div>
  <div class="abs chip" style="left:255px;top:641px;width:68px">file1.doc<b>X</b></div>
  <div class="abs chip" style="left:331px;top:641px;width:68px">file1.doc<b>X</b></div>
  <div class="abs chip" style="left:408px;top:641px;width:69px">file1.doc<b>X</b></div>

  <!-- Coordinator -->
  <div class="abs label req" style="left:24px;top:676px">Coordinator</div>
  <div class="abs ico" style="left:203px;top:669px"><svg width="30" height="30" viewBox="0 0 30 30" fill="#fff"><circle cx="15" cy="11" r="4"/><path d="M7 24c0-5 4-8 8-8s8 3 8 8z"/></svg></div>
  <div class="abs colon" style="left:239px;top:675px">:</div>
  <div class="abs btn" style="left:255px;top:673px;width:65px">ADD</div>
  <div class="abs chip" style="left:255px;top:700px;width:99px">Alan Pryce HR<b>X</b></div>

  <!-- Related Person -->
  <div class="abs label req" style="left:24px;top:736px">Related Person</div>
  <div class="abs ico" style="left:203px;top:729px"><svg width="30" height="30" viewBox="0 0 30 30" fill="#fff"><circle cx="11" cy="12" r="3.5"/><circle cx="19" cy="12" r="3.5"/><path d="M4 23c0-4 3-6 7-6s7 2 7 6zM14 23c0-4 2-6 5-6s7 2 7 6z"/></svg></div>
  <div class="abs colon" style="left:239px;top:735px">:</div>
  <div class="abs btn" style="left:255px;top:733px;width:65px">ADD</div>
  <div class="abs chip" style="left:255px;top:757px;width:101px">Rita Vale (IT)<b>X</b></div>
  <div class="abs chip" style="left:359px;top:757px;width:119px">Owen Lark (Finance)<b>X</b></div>
  <div class="abs chip" style="left:255px;top:776px;width:126px">Paul Reyes (Finance)<b>X</b></div>

  <!-- Remark -->
  <div class="abs label" style="left:24px;top:815px">Remark</div>
  <div class="abs ico" style="left:203px;top:808px"><svg width="30" height="30" viewBox="0 0 30 30" fill="#fff"><path d="M6 8h18v11H13l-4 4v-4H6z" fill="none" stroke="#fff" stroke-width="2"/><circle cx="11" cy="13.5" r="1.3"/><circle cx="15" cy="13.5" r="1.3"/><circle cx="19" cy="13.5" r="1.3"/></svg></div>
  <div class="abs colon" style="left:239px;top:814px">:</div>
  <div class="abs field area" style="left:253px;top:806px;width:233px">Lorem ipsum dolor sit amet</div>

  <!-- Related Request -->
  <div class="abs label" style="left:24px;top:915px">Related Request</div>
  <div class="abs ico" style="left:203px;top:908px"><svg width="30" height="30" viewBox="0 0 30 30" fill="#fff"><ellipse cx="13" cy="13" rx="7" ry="5"/><path d="M9 16l-2 4 5-3z"/><ellipse cx="19" cy="18" rx="5" ry="4" opacity=".8"/></svg></div>
  <div class="abs colon" style="left:239px;top:914px">:</div>
  <div class="abs related">
    <table>
      <thead><tr><th>Request No.</th><th>Request Date</th><th>Company</th><th>Branch</th></tr></thead>
      <tbody>
        <tr><td colspan="4" style="height:5px"></td></tr>
        <tr><td><a>AB56001</a></td><td>20/4/2013</td><td>NVC</td><td>GC1</td></tr>
        <tr><td><a>BIO5502</a></td><td>21/4/2013</td><td>NVC</td><td>GC2</td></tr>
        <tr><td><a>AB56001</a></td><td>20/4/2013</td><td>XYZ</td><td>GC3</td></tr>
        <tr><td><a>BIO5502</a></td><td>21/4/2013</td><td>XYZ</td><td>GC4</td></tr>
      </tbody>
    </table>
  </div>
  <div class="abs pager off" style="left:395px;top:1051px;width:44px">PREV</div>
  <div class="abs pager off" style="left:444px;top:1051px;width:23px">1</div>
  <div class="abs pager" style="left:469px;top:1051px;width:23px">2</div>
  <div class="abs pager" style="left:494px;top:1051px;width:23px">3</div>
  <div class="abs pager" style="left:517px;top:1051px;width:23px">4</div>
  <div class="abs pager" style="left:540px;top:1051px;width:23px">5</div>
  <div class="abs pager off" style="left:568px;top:1051px;width:43px">NEXT</div>

  <div class="abs action" style="left:254px;top:1092px;width:101px"><svg width="12" height="14" viewBox="0 0 12 14" style="position:absolute;left:15px;top:8px"><path d="M9 1L3 7l6 6" fill="none" stroke="#555" stroke-width="2.5"/></svg><span style="margin-left:26px">BACK</span></div>
  <div class="abs action" style="left:365px;top:1092px;width:248px">CREATE NEW REQUEST</div>

  <footer class="abs footer">
    <span style="left:48px">Copyright © 2013 Norvale Chemical. All rights reserved.</span>
    <span style="right:48px">Terms and Condition | Privacy</span>
  </footer>

</div>
</body>
</html>
```